App Design for Restaurant App

We need a design for the new Mobile App for the Restaurant Velmo. See attachment for presentation sketches.
There are two attached files: File 2 shows the App in general and File 1 shows the five screens which need to be designed. Your work should contain the general color scheme, icons and layout proposal.
Updates
Hi Designers
There where several questions about the scope of the work. We are looking for a design for an App. The promotion website of the restaurant Velmo can be found under www.restaurant-velmo.example
There you will get an impression of the Corporate Identity used by the restaurant and you will also find the logo.
In the sketch there are several screens which don't need a design, e.g. the cover flow or video screen
please ask if you have any question
kind regards
Tobias
Industry/Entity Type
Restaurant
Look and feel
Each slider illustrates characteristics of the customer's brand and the style your logo design should communicate.

```html
<!DOCTYPE html>
<html lang="de">
<head>
<meta charset="utf-8">
<title>Restaurant Velmo – App Startseite</title>
<link href="https://fonts.googleapis.com/css2?family=Hammersmith+One&display=swap" rel="stylesheet">
<style>
  :root{
    --stage:#12160a;
    --frame:#1b1f14;
    --cream:#fffbd0;
    --green-light:#6f8330;
    --green-mid:#4f6422;
    --green-dark:#34451a;
    --icon:#1e2410;
    --label:#fff8cc;
    --photo-red:#a8302a;
    --photo-warm:#c9b494;
  }
  html,body{margin:0;padding:0;}
  body{
    width:711px;height:1200px;overflow:hidden;
    background:var(--stage);
    font-family:"Hammersmith One",Arial,sans-serif;
    position:relative;
  }
  .app-screen{
    position:absolute;left:116px;top:218px;width:486px;height:736px;
    background:var(--frame);overflow:hidden;
  }
  .hero-photo{
    position:absolute;left:0;top:7px;width:486px;height:210px;
    background:
      linear-gradient(180deg,rgba(60,40,30,.35),rgba(0,0,0,.15)),
      linear-gradient(90deg,#7a6a55 0%,var(--photo-warm) 25%,var(--photo-red) 45%,#e9e2d6 60%,var(--photo-red) 80%,#5a3a30 100%);
  }
  .brand-badge{
    position:absolute;left:188px;top:7px;width:124px;height:103px;
    background:var(--cream);
    display:flex;flex-direction:column;align-items:center;justify-content:center;gap:8px;
  }
  .brand-badge .brand-mark{width:22px;height:22px;background:var(--green-dark);}
  .brand-badge .brand-name{font-size:10px;letter-spacing:1px;color:var(--green-dark);text-transform:uppercase;}
  .menu-panel{
    position:absolute;left:0;top:217px;width:486px;height:519px;
    background:radial-gradient(ellipse at 35% 15%,var(--green-light) 0%,var(--green-mid) 45%,var(--green-dark) 100%);
  }
  .menu-panel::before{
    content:"";position:absolute;left:0;top:0;right:0;height:10px;
    background:linear-gradient(180deg,rgba(0,0,0,.35),rgba(0,0,0,0));
  }
  .menu-item{
    position:absolute;width:150px;text-align:center;
  }
  .menu-item svg{display:block;margin:0 auto;width:36px;height:36px;fill:var(--icon);}
  .menu-item .label{
    display:block;margin-top:6px;font-size:19px;color:var(--label);
    text-shadow:0 1px 2px rgba(0,0,0,.5);
  }
  .menu-item .underline{
    display:block;margin:12px auto 0;width:120px;height:3px;border-radius:2px;
    background:radial-gradient(ellipse,rgba(0,0,0,.35),rgba(0,0,0,0) 70%);
  }
  .col-1{left:8px}.col-2{left:164px}.col-3{left:316px}
  .row-1{top:47px}.row-2{top:172px}.row-3{top:290px}
  .wave{position:absolute;left:0;top:0;width:486px;height:736px;}
</style>
</head>
<body>
<main class="app-screen">
  <div class="hero-photo" role="img" aria-label="Festlich gedeckter Restaurantsaal mit Weihnachtsbaum und roten Stuhlhussen"></div>
  <div class="brand-badge">
    <span class="brand-mark"></span>
    <span class="brand-name">Restaurant Velmo</span>
  </div>

  <nav class="menu-panel">
    <a class="menu-item col-1 row-1">
      <svg viewBox="0 0 36 36"><circle cx="18" cy="18" r="17"/><rect x="16" y="15" width="4" height="13" fill="#5d7228"/><circle cx="18" cy="10" r="2.4" fill="#5d7228"/></svg>
      <span class="label">Aktuell</span><span class="underline"></span>
    </a>
    <a class="menu-item col-2 row-1">
      <svg viewBox="0 0 36 36"><rect x="9" y="2" width="18" height="26" rx="3"/><circle cx="18" cy="13" r="5" fill="#5d7228"/><circle cx="18" cy="13" r="2.2"/><rect x="11" y="30" width="14" height="4" rx="1"/></svg>
      <span class="label">WebCam</span><span class="underline"></span>
    </a>
    <a class="menu-item col-3 row-1">
      <svg viewBox="0 0 36 36"><circle cx="18" cy="18" r="17"/><rect x="12" y="7" width="2" height="8" fill="#5d7228"/><rect x="15" y="7" width="2" height="8" fill="#5d7228"/><rect x="12" y="13" width="5" height="3" fill="#5d7228"/><rect x="13.5" y="15" width="2" height="14" fill="#5d7228"/><path d="M21 7c3 0 4 4 4 8h-2v14h-2z" fill="#5d7228"/></svg>
      <span class="label">Restaurant</span><span class="underline"></span>
    </a>

    <a class="menu-item col-1 row-2">
      <svg viewBox="0 0 36 36"><path d="M18 1C10 1 5 7 5 13c0 9 13 22 13 22s13-13 13-22C31 7 26 1 18 1z"/><circle cx="18" cy="13" r="4.5" fill="#5d7228"/></svg>
      <span class="label">Events</span><span class="underline"></span>
    </a>
    <a class="menu-item col-2 row-2">
      <svg viewBox="0 0 36 36"><rect x="2" y="5" width="32" height="29" rx="3"/><rect x="9" y="1" width="3" height="7"/><rect x="24" y="1" width="3" height="7"/><rect x="5" y="13" width="26" height="18" fill="#5d7228"/><text x="18" y="27" font-size="11" text-anchor="middle" fill="#1e2410" font-family="Arial,sans-serif">12</text></svg>
      <span class="label">Reservation</span><span class="underline"></span>
    </a>
    <a class="menu-item col-3 row-2">
      <svg viewBox="0 0 36 36"><rect x="1" y="3" width="7" height="6" rx="1.5"/><rect x="11" y="3" width="24" height="6" rx="1.5"/><rect x="1" y="15" width="7" height="6" rx="1.5"/><rect x="11" y="15" width="24" height="6" rx="1.5"/><rect x="1" y="27" width="7" height="6" rx="1.5"/><rect x="11" y="27" width="24" height="6" rx="1.5"/></svg>
      <span class="label">Menukarte</span><span class="underline"></span>
    </a>

    <a class="menu-item col-1 row-3">
      <svg viewBox="0 0 36 36"><path d="M2 10h8l3-4h10l3 4h8v22H2z"/><circle cx="18" cy="20" r="7" fill="#5d7228"/><circle cx="18" cy="20" r="4"/></svg>
      <span class="label">Galerie</span><span class="underline"></span>
    </a>
    <a class="menu-item col-2 row-3">
      <svg viewBox="0 0 36 36"><path d="M32 3 4 16l13 3 3 13z"/></svg>
      <span class="label">Anfahrt</span><span class="underline"></span>
    </a>
    <a class="menu-item col-3 row-3">
      <svg viewBox="0 0 36 36"><path d="M2 6l10-3 12 3 10-3v27l-10 3-12-3-10 3z"/></svg>
      <span class="label">Gastebuch</span><span class="underline"></span>
    </a>
  </nav>

  <svg class="wave" viewBox="0 0 486 736" aria-hidden="true">
    <path d="M0 630 C110 580 210 615 310 600 C400 588 455 560 486 540 L486 736 L0 736Z" fill="#2c3a14"/>
    <path d="M0 657 C110 612 210 640 310 628 C400 618 455 595 486 580 L486 736 L0 736Z" fill="var(--cream)"/>
  </svg>
</main>
</body>
</html>
```